Recipe Card Design

I have a small kitchen store in Livingston Montana, and I would like to have recipe cards (4x6 postcard) designed with my logo, lines for recipe writing, all in black and white. My website is here: www.brambleforkpantry.com

Store

```html
<!DOCTYPE html>
<html lang="en">
<head>
<meta charset="utf-8">
<title>Recipe Card – Bramble Fork Pantry</title>
<link rel="stylesheet" href="https://fonts.googleapis.com/css2?family=Amatic+SC:wght@400;700&family=Dancing+Script:wght@500&family=Lobster+Two:wght@700&family=Roboto+Slab:wght@400&display=swap">
<style>
  :root {
    --ink: #1b1b1b;
    --paper: #ffffff;
    --backdrop: #e9e9e7;
    --rule: #3a3a3a;
  }
  html, body {
    margin: 0;
    width: 1200px;
    height: 960px;
    overflow: hidden;
    background: var(--backdrop);
  }
  .postcard {
    position: absolute;
    left: 276px;
    width: 1080px;
    height: 720px;
    background: var(--paper);
    color: var(--ink);
    box-shadow: 0 3px 14px rgba(0,0,0,0.16);
    transform: scale(0.6);
    transform-origin: top left;
  }
  .postcard-front { top: 36px; }
  .postcard-back { top: 492px; }

  .card-frame {
    position: absolute;
    inset: 0;
  }
  .divider {
    position: absolute;
    left: 545px;
    top: 80px;
    width: 2px;
    height: 560px;
    background: var(--rule);
  }

  /* Slogan */
  .slogan {
    position: absolute;
    left: 80px;
    top: 170px;
    width: 420px;
    margin: 0;
    text-align: center;
    font-weight: normal;
  }
  .slogan-healthy {
    display: block;
    font-family: "Lobster Two", cursive;
    font-weight: 700;
    font-size: 120px;
    line-height: 1;
    letter-spacing: 1px;
  }
  .slogan-outside {
    display: flex;
    align-items: center;
    justify-content: center;
    gap: 10px;
    font-family: "Amatic SC", sans-serif;
    font-weight: 400;
    font-size: 58px;
    line-height: 0.9;
    letter-spacing: 3px;
    margin-top: -6px;
  }
  .slogan-outside::before,
  .slogan-outside::after {
    content: "";
    width: 40px;
    height: 2px;
    background: var(--ink);
  }
  .slogan-inside {
    display: flex;
    align-items: baseline;
    justify-content: center;
    gap: 8px;
  }
  .slogan-connector {
    font-family: "Dancing Script", cursive;
    font-size: 30px;
  }
  .slogan-inside-word {
    font-family: "Amatic SC", sans-serif;
    font-size: 64px;
    letter-spacing: 3px;
    line-height: 0.9;
  }

  /* Website */
  .visit {
    position: absolute;
    left: 90px;
    top: 560px;
    margin: 0;
    font-family: "Amatic SC", sans-serif;
    font-weight: 700;
    font-size: 28px;
    letter-spacing: 2px;
    line-height: 1.05;
    text-transform: uppercase;
  }
  .visit-url { display: block; }

  /* Brand */
  .brand {
    position: absolute;
    left: 720px;
    top: 52px;
    display: flex;
    align-items: center;
    gap: 10px;
    font-family: "Amatic SC", sans-serif;
    font-weight: 700;
    font-size: 30px;
    letter-spacing: 2px;
  }
  .brand-mark {
    width: 22px;
    height: 22px;
    background: var(--ink);
  }

  /* Writing area */
  .writing-area {
    position: absolute;
    left: 580px;
    top: 150px;
    width: 430px;
  }
  .field {
    display: flex;
    align-items: flex-end;
    height: 40px;
    font-family: "Amatic SC", sans-serif;
    font-weight: 700;
    font-size: 28px;
    letter-spacing: 2px;
    text-transform: uppercase;
  }
  .field-label {
    padding-right: 10px;
    line-height: 1;
  }
  .field-line,
  .write-line {
    flex: 1;
    border-bottom: 2px solid var(--rule);
    height: 0;
    margin-bottom: 4px;
  }
  .write-line {
    display: block;
    margin: 38px 0 0 70px;
  }
  .field-instructions { margin-top: 38px; }

  /* Back side */
  .stamp-box {
    position: absolute;
    left: 830px;
    top: 50px;
    width: 180px;
    height: 170px;
    border: 3px solid var(--ink);
    box-sizing: border-box;
  }
  .address-lines {
    position: absolute;
    left: 560px;
    top: 290px;
    width: 450px;
  }
  .address-line {
    display: block;
    border-bottom: 3px solid var(--ink);
    margin-bottom: 62px;
  }
  .message-panel {
    position: absolute;
    left: 60px;
    top: 430px;
    width: 440px;
    height: 210px;
    margin: 0;
    padding: 26px 28px;
    box-sizing: border-box;
    border: 3px solid var(--ink);
    font-family: "Roboto Slab", serif;
    font-size: 24px;
    line-height: 1.35;
    color: #4a4a4a;
  }
</style>
</head>
<body>
  <article class="postcard postcard-front">
    <svg class="card-frame" width="1080" height="720" viewBox="0 0 1080 720" aria-hidden="true">
      <path d="M58 26 H1022 A32 32 0 0 0 1054 58 V662 A32 32 0 0 0 1022 694 H58 A32 32 0 0 0 26 662 V58 A32 32 0 0 0 58 26 Z"
            fill="none" stroke="#1b1b1b" stroke-width="4"/>
      <path d="M64 40 H1016 A26 26 0 0 0 1040 64 V656 A26 26 0 0 0 1016 680 H64 A26 26 0 0 0 40 656 V64 A26 26 0 0 0 64 40 Z"
            fill="none" stroke="#1b1b1b" stroke-width="1.5"/>
      <circle cx="26" cy="26" r="20" fill="#1b1b1b"/>
      <circle cx="1054" cy="26" r="20" fill="#1b1b1b"/>
      <circle cx="26" cy="694" r="20" fill="#1b1b1b"/>
      <circle cx="1054" cy="694" r="20" fill="#1b1b1b"/>
    </svg>

    <h1 class="slogan">
      <span class="slogan-healthy">Healthy</span>
      <span class="slogan-outside">Outside</span>
      <span class="slogan-inside">
        <span class="slogan-connector">starts from the</span>
        <span class="slogan-inside-word">Inside</span>
      </span>
    </h1>

    <p class="visit">
      Visit for more:
      <span class="visit-url">www.brambleforkpantry.com</span>
    </p>

    <div class="divider"></div>

    <div class="brand">
      <span class="brand-mark"></span>
      <span class="brand-name">Bramble Fork Pantry</span>
    </div>

    <section class="writing-area">
      <div class="field"><span class="field-label">Recipe:</span><span class="field-line"></span></div>
      <div class="field"><span class="field-label">Ingredients:</span><span class="field-line"></span></div>
      <span class="write-line"></span>
      <span class="write-line"></span>
      <div class="field field-instructions"><span class="field-label">Instructions:</span><span class="field-line"></span></div>
      <span class="write-line"></span>
      <span class="write-line"></span>
      <span class="write-line"></span>
      <span class="write-line"></span>
      <span class="write-line"></span>
    </section>
  </article>

  <article class="postcard postcard-back">
    <div class="stamp-box"></div>
    <div class="address-lines">
      <span class="address-line"></span>
      <span class="address-line"></span>
      <span class="address-line"></span>
      <span class="address-line"></span>
    </div>
    <p class="message-panel">Every recipe tells a story. Share yours with family and friends, one handwritten card at a time. Stop by the shop for tools, spices and ideas for your next favourite meal.</p>
  </article>
</body>
</html>
```